Human Resource Consultant's Website needs an Updated Look

I'm an HR Consultant based in Denver that caters to small business owners. I like my logo, and the existing content (though open to editorial suggestions) but would like to reformat my site and possibly update graphics. I want to be able to manage content moving forward. TLMWAdvisory.com

Target Market(s)

Small business owners with 10-500 employees in Metro Denver

Coding

Coded - Design and coding required

Font styles to use
Other font styles liked:
• Closer to existing font but open to suggestions

Colors

Designer to choose colors to be used in the design.

Requirements
Must have
• Links on landing page to other pages
• Visual appeal to younger demographic found in the small to medium sized business owner
• Scroll down rather than use the clunky "ladder" tabs I see now
• Color palate that compliments logo
Nice to have
• Pages that scroll down, links to page content on the first page,
Should not have
• Hate the standard employee-employer photos on most HR websites. Would prefer to use illustrations over the typical photos

```html
<!DOCTYPE html>
<html lang="en">
<head>
<meta charset="utf-8">
<title>TLMW ~ HR Advisory</title>
<link href="https://fonts.googleapis.com/css2?family=Cinzel:wght@400;700&family=Arimo:wght@400;700&display=swap" rel="stylesheet">
<style>
:root{
  --green:#8dc63f;
  --green-dark:#5f9e25;
  --navy:#1c4d7c;
  --footer:#154f85;
  --ink:#444;
  --heading:#1f4e79;
  --hero-bg:#e7f1fb;
  --soft:#f4f4f4;
  --line:#dcdcdc;
}
*{box-sizing:border-box;margin:0;padding:0}
html,body{width:1200px;height:3066px;overflow:hidden}
body{font-family:"Arimo",Arial,sans-serif;color:var(--ink);background:#fff;position:relative}
.abs{position:absolute}
.serif{font-family:"Cinzel",Georgia,serif}
.green-rule{width:72px;height:3px;background:var(--green);margin-top:12px}
.center-rule{width:72px;height:3px;background:var(--green);margin:12px auto 0}

/* header */
.site-header{left:0;top:0;width:1200px;height:106px;border-top:4px solid var(--green);background:#fff;border-bottom:1px solid #eee}
.brand{left:86px;top:22px;display:flex;align-items:center;gap:12px}
.brand-mark{width:52px;height:52px;border-radius:50%;background:var(--navy)}
.brand-name{font-family:"Cinzel",Georgia,serif;font-size:24px;font-weight:700;color:var(--navy);line-height:1}
.call{right:86px;top:20px;display:flex;align-items:center;gap:10px;font-family:"Cinzel",Georgia,serif;color:var(--green);font-size:19px}
.call-icon{width:40px;height:40px;border-radius:50%;background:var(--green);display:flex;align-items:center;justify-content:center}
.main-nav{right:86px;top:72px;display:flex;gap:44px;font-family:"Cinzel",Georgia,serif;font-size:14px;color:#333}
.main-nav a{color:inherit;text-decoration:none}
.main-nav a.active{color:var(--green)}

/* hero */
.hero{left:0;top:106px;width:1200px;height:511px;background:linear-gradient(180deg,#f3f8fd,var(--hero-bg))}
.hero-art{left:552px;top:20px;width:640px;height:470px;border-radius:48% 40% 30% 44%;background:radial-gradient(circle at 55% 45%,#9cc3ee,#cfe1f6 60%,transparent 72%)}
.hero-text{left:86px;top:160px;width:460px}
.hero-text h1{font-family:"Cinzel",Georgia,serif;color:var(--green);font-size:26px;font-weight:700;letter-spacing:.5px}
.hero-text h2{font-family:"Cinzel",Georgia,serif;color:var(--heading);font-size:19px;font-weight:700;margin-top:16px}
.hero-text p{font-size:12.5px;line-height:27px;margin-top:18px;color:#555}
.btn{display:inline-block;background:var(--green);color:#fff;font-family:"Cinzel",Georgia,serif;font-weight:700;font-size:14px;padding:12px 18px;text-decoration:none}
.hero-text .btn{margin-top:22px}

/* approach */
.approach{left:0;top:617px;width:1200px;height:487px;background:#fff}
.approach-text{left:86px;top:42px;width:482px}
.section-title{font-family:"Cinzel",Georgia,serif;color:var(--heading);font-size:30px;font-weight:700}
.approach-text p{font-size:12.5px;line-height:26px;margin-top:26px;color:#555}
.pillars{margin-top:22px;list-style:none;font-size:12px;line-height:21px;color:#555}
.pillars li{margin-bottom:18px}
.pillars b{color:var(--green);font-weight:700}
.approach-art{left:0;top:0}

/* services */
.services{left:0;top:1104px;width:1200px;height:644px;background:var(--soft)}
.intro{text-align:center;font-size:12px;color:#555;margin-top:22px}
.service-card{top:178px;width:331px;height:400px;background:#fff;border:1px solid var(--line);overflow:hidden}
.service-icon{width:122px;height:122px;border-radius:50%;margin:24px auto 0;display:flex;align-items:center;justify-content:center;border:6px solid #fff;box-shadow:0 0 0 3px currentColor}
.service-card h3{font-family:"Cinzel",Georgia,serif;font-size:16px;color:#333;text-align:center;margin-top:26px;letter-spacing:.5px}
.service-card ul{list-style:none;margin:22px 0 0 46px;font-size:12px;color:#444}
.service-card li{height:34px;display:flex;align-items:center;gap:20px}
.corner{right:0;bottom:0}

/* blog */
.blog{left:0;top:1748px;width:1200px;height:456px;background:#fff}
.post{top:172px;width:500px;height:218px;border:1px solid var(--line);background:#fff}
.post-art{left:8px;top:8px;width:178px;height:200px}
.post-body{left:216px;top:24px;width:270px}
.post-body h4{font-family:"Cinzel",Georgia,serif;font-size:15px;color:#333;font-weight:400}
.post-date{font-family:"Cinzel",Georgia,serif;color:var(--green);font-size:13px;margin-top:10px;display:flex;align-items:center;gap:6px}
.post-body p{font-size:11.5px;line-height:22px;color:#666;margin-top:10px}
.post-body .btn{margin-top:14px;font-size:12px;padding:11px 18px}

/* contact */
.contact{left:0;top:2204px;width:1200px;height:542px;background:var(--soft)}
.contact-text{left:86px;top:40px;width:440px}
.contact-text p{font-size:12px;line-height:28px;color:#555;margin-top:26px}
.field{width:419px;height:46px;border:1px solid #ccc;background:#fff;font-size:12px;color:#444;padding:14px 14px;margin-top:6px}
.field.first{margin-top:22px}
.field.message{height:70px}
.contact-text .btn{margin-top:26px;font-size:14px;padding:12px 26px}
.contact-art{left:593px;top:34px;width:531px;height:460px;background:linear-gradient(180deg,#eef0f3,#d9dde3);border-radius:6px}

/* footer */
.site-footer{left:0;top:2746px;width:1200px;height:320px;background:var(--footer);color:#fff}
.footer-brand{left:0;top:36px;width:1200px;display:flex;justify-content:center;align-items:center;gap:12px}
.footer-brand .brand-mark{background:#fff}
.footer-brand .brand-name{color:#fff}
.info{top:140px;display:flex;gap:18px;align-items:center}
.info-icon{width:56px;height:56px;border-radius:50%;border:1px solid rgba(255,255,255,.7);display:flex;align-items:center;justify-content:center}
.info h5{font-size:17px;font-weight:700}
.info p{font-size:11.5px;font-weight:700;line-height:20px;margin-top:4px}
.footer-rule{left:86px;top:240px;width:1028px;height:1px;background:rgba(255,255,255,.25)}
.copyright{left:86px;top:273px;font-size:11.5px}
.social{right:88px;top:262px;display:flex;gap:10px}
.social span{width:36px;height:36px;border-radius:50%;border:1px solid #fff;display:block}
</style>
</head>
<body>

<header class="site-header abs">
  <div class="brand abs"><span class="brand-mark"></span><span class="brand-name">TLMW ~ HR Advisory</span></div>
  <div class="call abs">
    <span class="call-icon"><svg width="18" height="18" viewBox="0 0 24 24"><path fill="#fff" d="M6.6 10.8a15 15 0 0 0 6.6 6.6l2.2-2.2c.3-.3.7-.4 1-.2 1.1.4 2.3.6 3.6.6.6 0 1 .4 1 1V20c0 .6-.4 1-1 1A17 17 0 0 1 3 4c0-.6.4-1 1-1h3.5c.6 0 1 .4 1 1 0 1.3.2 2.5.6 3.6.1.3 0 .7-.2 1z"/></svg></span>
    CALL US : 720.555.0148
  </div>
  <nav class="main-nav abs"><a class="active" href="#">Home</a><a href="#">My Approach</a><a href="#">My Services</a><a href="#">Dana</a><a href="#">Contact Me</a></nav>
</header>

<section class="hero abs">
  <div class="hero-art abs" role="img" aria-label="Illustration of a team analysing data around a large laptop with charts and magnifying glasses"></div>
  <div class="hero-text abs">
    <h1>HR &amp; Business Consultant</h1>
    <h2>Trainer &amp; Facilitator – Project Manager</h2>
    <p>Work with a Human Resources Consultant, with a career grounded in business, who understands how every aspect of HR affects the bottom line.&nbsp; I will partner with you to...Human capital is the wealth an organization possesses</p>
    <a class="btn" href="#">Read More</a>
  </div>
</section>

<section class="approach abs">
  <svg class="approach-art abs" width="1200" height="487" role="img" aria-label="Illustration of two colleagues working at an office desk">
    <defs><linearGradient id="approachGreen" x1="0" y1="0" x2="1" y2="1"><stop offset="0" stop-color="#a3d255"/><stop offset="1" stop-color="#5fa52a"/></linearGradient></defs>
    <polygon points="718,17 1200,17 1200,471 562,471" fill="url(#approachGreen)"/>
  </svg>
  <div class="approach-text abs">
    <h2 class="section-title">My Approach</h2>
    <div class="green-rule"></div>
    <p>Entrepreneurs are innovative risk-taking business leaders. You had an idea and ran with it! But when you looked back, were your employees following If not, partner with me to I cons ult with small to medium sized business owners to support, complement or develop their skill set in talent management.</p>
    <ul class="pillars">
      <li><b>STRATEGY</b> : setting goals and leading individuals and teams towards aligned successful results</li>
      <li><b>COMMUNICATION</b> : crystallizing messages to individuals and groups</li>
      <li><b>HUMAN RESOURCES EXPERTISE</b> : building knowledge of HR laws, regulations, and best practices</li>
      <li><b>ETHICS</b> : exploring efforts to balance the needs of people, profit and planet</li>
    </ul>
  </div>
</section>

<section class="services abs">
  <h2 class="section-title" style="text-align:center;margin-top:52px">My Services</h2>
  <div class="center-rule"></div>
  <p class="intro">Work with a Human Resources Consultant, with a career grounded in business, who understands</p>

  <article class="service-card abs" style="left:86px">
    <div class="service-icon" style="background:var(--green);color:var(--green)"><svg width="60" height="60" viewBox="0 0 60 60" fill="none" stroke="#fff" stroke-width="3"><rect x="10" y="22" width="40" height="10"/><line x1="30" y1="32" x2="30" y2="48"/><circle cx="20" cy="12" r="5"/><circle cx="40" cy="12" r="5"/></svg></div>
    <h3>HR &amp; Business Consultant</h3>
    <ul>
      <li><svg width="12" height="10"><path d="M1 5l4 4 6-8" stroke="#8dc63f" stroke-width="2.4" fill="none"/></svg>Strategic Planning</li>
      <li><svg width="12" height="10"><path d="M1 5l4 4 6-8" stroke="#8dc63f" stroke-width="2.4" fill="none"/></svg>Employment Law</li>
      <li><svg width="12" height="10"><path d="M1 5l4 4 6-8" stroke="#8dc63f" stroke-width="2.4" fill="none"/></svg>Conflict Resolution</li>
      <li><svg width="12" height="10"><path d="M1 5l4 4 6-8" stroke="#8dc63f" stroke-width="2.4" fill="none"/></svg>Investigations</li>
      <li><svg width="12" height="10"><path d="M1 5l4 4 6-8" stroke="#8dc63f" stroke-width="2.4" fill="none"/></svg>Terminations</li>
    </ul>
    <svg class="corner abs" width="66" height="66"><polygon points="66,0 66,66 0,66" fill="#8dc63f"/><circle cx="46" cy="46" r="9" fill="#fff"/><path d="M44 41l5 5-5 5" stroke="#8dc63f" stroke-width="2.4" fill="none"/></svg>
  </article>

  <article class="service-card abs" style="left:433px">
    <div class="service-icon" style="background:var(--navy);color:var(--navy)"><svg width="60" height="60" viewBox="0 0 60 60" fill="none" stroke="#fff" stroke-width="3"><circle cx="30" cy="12" r="5"/><circle cx="14" cy="36" r="4"/><circle cx="30" cy="36" r="4"/><circle cx="46" cy="36" r="4"/><path d="M8 50c0-6 12-6 12 0M24 50c0-6 12-6 12 0M40 50c0-6 12-6 12 0"/></svg></div>
    <h3>HR Project Manager</h3>
    <ul>
      <li><svg width="12" height="10"><path d="M1 5l4 4 6-8" stroke="#1c4d7c" stroke-width="2.4" fill="none"/></svg>Financial Analysis of HR Metrics</li>
      <li><svg width="12" height="10"><path d="M1 5l4 4 6-8" stroke="#1c4d7c" stroke-width="2.4" fill="none"/></svg>Talent SWOT Analysis</li>
      <li><svg width="12" height="10"><path d="M1 5l4 4 6-8" stroke="#1c4d7c" stroke-width="2.4" fill="none"/></svg>Strategic Compensation</li>
      <li><svg width="12" height="10"><path d="M1 5l4 4 6-8" stroke="#1c4d7c" stroke-width="2.4" fill="none"/></svg>Managing Change Initiatives</li>
      <li><svg width="12" height="10"><path d="M1 5l4 4 6-8" stroke="#1c4d7c" stroke-width="2.4" fill="none"/></svg>Investigations</li>
    </ul>
    <svg class="corner abs" width="66" height="66"><polygon points="66,0 66,66 0,66" fill="#1c4d7c"/><circle cx="46" cy="46" r="9" fill="#fff"/><path d="M44 41l5 5-5 5" stroke="#1c4d7c" stroke-width="2.4" fill="none"/></svg>
  </article>

  <article class="service-card abs" style="left:781px">
    <div class="service-icon" style="background:var(--green);color:var(--green)"><svg width="60" height="60" viewBox="0 0 60 60" fill="none" stroke="#fff" stroke-width="3"><rect x="22" y="6" width="30" height="20"/><circle cx="14" cy="22" r="5"/><circle cx="18" cy="44" r="4"/><circle cx="32" cy="44" r="4"/><circle cx="46" cy="44" r="4"/></svg></div>
    <h3>Trainer and Facilitator</h3>
    <ul>
      <li><svg width="12" height="10"><path d="M1 5l4 4 6-8" stroke="#8dc63f" stroke-width="2.4" fill="none"/></svg>HR's Impact on the Bottom Line</li>
      <li><svg width="12" height="10"><path d="M1 5l4 4 6-8" stroke="#8dc63f" stroke-width="2.4" fill="none"/></svg>Human Capital Strategies</li>
      <li><svg width="12" height="10"><path d="M1 5l4 4 6-8" stroke="#8dc63f" stroke-width="2.4" fill="none"/></svg>Employment Law</li>
      <li><svg width="12" height="10"><path d="M1 5l4 4 6-8" stroke="#8dc63f" stroke-width="2.4" fill="none"/></svg>Leadership Competencies</li>
      <li><svg width="12" height="10"><path d="M1 5l4 4 6-8" stroke="#8dc63f" stroke-width="2.4" fill="none"/></svg>Vision/Mission/Value Statements</li>
    </ul>
    <svg class="corner abs" width="66" height="66"><polygon points="66,0 66,66 0,66" fill="#8dc63f"/><circle cx="46" cy="46" r="9" fill="#fff"/><path d="M44 41l5 5-5 5" stroke="#8dc63f" stroke-width="2.4" fill="none"/></svg>
  </article>
</section>

<section class="blog abs">
  <h2 class="section-title" style="text-align:center;margin-top:52px">Our Dana</h2>
  <div class="center-rule"></div>
  <p class="intro">Work with a Human Resources Consultant, with a career grounded in business, who understands</p>

  <article class="post abs" style="left:86px">
    <div class="post-art abs" role="img" aria-label="Illustration of people holding colourful puzzle pieces" style="background:linear-gradient(135deg,#2a9d8f,#1d6f7a)"></div>
    <div class="post-body abs">
      <h4>Beyond Comp &amp; Benefits….</h4>
      <div class="post-date"><svg width="12" height="12"><rect x="1" y="2" width="10" height="9" fill="none" stroke="#8dc63f" stroke-width="1.5"/><line x1="1" y1="5" x2="11" y2="5" stroke="#8dc63f" stroke-width="1.5"/></svg>September 2, 2018</div>
      <p>What do small business owners need to know to round out a "Total Rewards" strategy?&nbsp; For those not your talent, your employees.</p>
      <a class="btn" href="#">Read More</a>
    </div>
  </article>

  <article class="post abs" style="left:613px">
    <div class="post-art abs" role="img" aria-label="Word cloud about organizational culture" style="background:linear-gradient(135deg,#eef0f2,#c9d0d8)"></div>
    <div class="post-body abs">
      <h4>Organizational Culture</h4>
      <div class="post-date"><svg width="12" height="12"><rect x="1" y="2" width="10" height="9" fill="none" stroke="#8dc63f" stroke-width="1.5"/><line x1="1" y1="5" x2="11" y2="5" stroke="#8dc63f" stroke-width="1.5"/></svg>August 1, 2018</div>
      <p>Today owners need to consider hiring the right person for the job and for the organization. It is not enough to find someone with the SKA's</p>
      <a class="btn" href="#">Read More</a>
    </div>
  </article>
</section>

<section class="contact abs">
  <div class="contact-text abs">
    <h2 class="section-title">Contact Me</h2>
    <div class="green-rule"></div>
    <p>Recently, I completed a Master's Degree in Human Resources Management with a Specialization in Organizational Leadership and have successfully applied my knowledge in the latest trends affecting HR and business today</p>
    <div class="field first">Name*</div>
    <div class="field">Email*</div>
    <div class="field">Phone*</div>
    <div class="field message">Message :</div>
    <a class="btn" href="#">Submit</a>
  </div>
  <div class="contact-art abs" role="img" aria-label="Illustration of a consultant working on a laptop at a desk"></div>
</section>

<footer class="site-footer abs">
  <div class="footer-brand abs"><span class="brand-mark"></span><span class="brand-name">TLMW ~ HR Advisory</span></div>

  <div class="info abs" style="left:118px">
    <span class="info-icon"><svg width="20" height="24" viewBox="0 0 20 24"><path d="M10 1a8 8 0 0 0-8 8c0 6 8 14 8 14s8-8 8-14a8 8 0 0 0-8-8z" fill="none" stroke="#fff" stroke-width="2"/><circle cx="10" cy="9" r="3" fill="#fff"/></svg></span>
    <div><h5>Address :</h5><p># 2152 Lorem Ipsum DUmmy Text<br>Lorem Ipsum Dummy</p></div>
  </div>
  <div class="info abs" style="left:512px">
    <span class="info-icon"><svg width="22" height="16"><rect x="1" y="1" width="20" height="14" fill="none" stroke="#fff" stroke-width="2"/><path d="M1 1l10 8 10-8" fill="none" stroke="#fff" stroke-width="2"/></svg></span>
    <div><h5>Email</h5><p>hello@TLMWAdvisory.com</p></div>
  </div>
  <div class="info abs" style="left:862px">
    <span class="info-icon"><svg width="20" height="20" viewBox="0 0 24 24"><path fill="#fff" d="M6.6 10.8a15 15 0 0 0 6.6 6.6l2.2-2.2c.3-.3.7-.4 1-.2 1.1.4 2.3.6 3.6.6.6 0 1 .4 1 1V20c0 .6-.4 1-1 1A17 17 0 0 1 3 4c0-.6.4-1 1-1h3.5c.6 0 1 .4 1 1 0 1.3.2 2.5.6 3.6.1.3 0 .7-.2 1z"/></svg></span>
    <div><h5>Phone</h5><p>Mobile : 720.555.0148</p></div>
  </div>

  <div class="footer-rule abs"></div>
  <p class="copyright abs">© Copyright-2018 TLMW ~ HR Advisory All rights reserved</p>
  <div class="social abs"><span></span><span></span></div>
</footer>

</body>
</html>
```